Business card design needed

Marketing Communications

Target Market(s)

prospective clients in the marketing communications industry

Industry/Entity Type

Business

Contact Information for Business Card

marel tusk
Marketing Communications
lorapen@tidewire.com
0493 518274

Logo Text

marel tusk

Logo styles of interest
Abstract Logo
Requirements
Must have
• An appropriate abstract logo. only a one or two colour design
Nice to have
• Logo to portray the growth of a marketing brief
Should not have
• no more than two colours maximum

```html
<!DOCTYPE html>
<html lang="en">
<head>
<meta charset="utf-8">
<title>Marel Tusk – Business Card</title>
<link rel="stylesheet" href="https://fonts.googleapis.com/css2?family=Questrial&display=swap">
<style>
  :root {
    --backdrop: #e8e9eb;
    --card-white: #fbfbfb;
    --brand-blue: #2f6fd6;
    --band-blue: #3474d8;
    --ribbon-soft: #7ea5de;
    --graphic-light: #d4e5fa;
    --graphic-deep: #6fa2e8;
    --ink-white: #ffffff;
  }
  html, body {
    margin: 0;
    padding: 0;
    width: 1000px;
    height: 1200px;
    overflow: hidden;
    background: var(--backdrop);
  }
  .canvas {
    position: relative;
    width: 1000px;
    height: 1200px;
    display: flex;
    align-items: center;
    justify-content: center;
  }
  .business-card {
    width: 810px;
    height: 490px;
    filter: drop-shadow(0 14px 24px rgba(0,0,0,0.18));
  }
  .card-text {
    font-family: "Questrial", "Century Gothic", sans-serif;
    fill: var(--ink-white);
  }
  .holder-name { font-size: 25px; letter-spacing: 0.5px; }
  .holder-role { font-size: 14.5px; }
  .contact-line { font-size: 12.5px; }
</style>
</head>
<body>
<main class="canvas">
  <svg class="business-card" viewBox="0 0 405 245" xmlns="http://www.w3.org/2000/svg" aria-label="Business card for Marel Tusk, Marketing Communications">
    <defs>
      <clipPath id="card-shape">
        <path d="M28 0 H405 V217 A28 28 0 0 1 377 245 H28 A28 28 0 0 1 0 217 V28 A28 28 0 0 1 28 0 Z"/>
      </clipPath>
      <linearGradient id="graphic-fill" x1="0" y1="1" x2="1" y2="0">
        <stop offset="0" stop-color="var(--graphic-deep)"/>
        <stop offset="1" stop-color="var(--graphic-light)"/>
      </linearGradient>
    </defs>

    <g clip-path="url(#card-shape)">
      <rect class="card-base" width="405" height="245" fill="var(--card-white)"/>

      <rect class="role-band" x="0" y="110" width="252" height="28" fill="var(--ribbon-soft)"/>
      <rect class="name-band" x="0" y="77" width="252" height="31" fill="var(--brand-blue)"/>

      <g class="growth-graphic" role="img" aria-label="Abstract growth graphic: a rising blue ribbon with steps">
        <rect x="252" y="0" width="153" height="138" fill="url(#graphic-fill)"/>
      </g>

      <text class="card-text holder-name" x="30" y="101">MAREL TUSK</text>
      <text class="card-text holder-role" x="30" y="130">Marketing Communications</text>

      <rect class="contact-band" x="0" y="190" width="405" height="55" fill="var(--band-blue)"/>

      <g class="mail-icon" fill="none" stroke="var(--ink-white)" stroke-width="1">
        <rect x="45" y="205" width="11" height="10" rx="1.5"/>
        <polyline points="46,207 50.5,211 55,207"/>
      </g>
      <text class="card-text contact-line" x="62" y="214">lorapen@tidewire.com</text>

      <g class="phone-icon">
        <circle cx="267" cy="210" r="6.5" fill="none" stroke="var(--ink-white)" stroke-width="1"/>
        <path d="M264.3 206.6 q-1 2.6 1.6 5.3 q2.5 2.3 4.9 1.5 l-1.3-1.6 q-1 .5-2.2-.6 q-1.2-1.2-.7-2.3 z" fill="var(--ink-white)"/>
      </g>
      <text class="card-text contact-line" x="279" y="214">0493 518274</text>
    </g>
  </svg>
</main>
</body>
</html>
```